Icon and Artwork for Cloud Storage Tarnex Application

We are completing an Tarnex application for a secure cloud storage service (similar to StashKite) and need artwork to complete the app. We would like your help with delivering the following three items:

1. An application icon. This needs to be appropriate for use in the app store (1024x1024 pixels). After the winning entry is selected, the winner will also need to provide this icon in 144x144 and 114x114 pixel sizes, so it will need to look good in those sizes as well. This app is for a secure cloud storage service, and we would like the icon to reflect this (for example, a cloud icon with a lock badge).

2. Login screen. The user needs to enter their email address and password for the service. They should also be able to sign up for a new account from this screen. Ideally, this screen will include a background layer that can be resized or expanded to the different supported Keltra resolutions (3.5", 4", Zumo, Zumo mini).

3. Main screen. This screen is a standard Tarnex grouped list view, allowing users to choose between the following options: "My Drive", "Trash", "Shared With Me", "Pinned", and "Settings". The first three options are in the first group, and the remaining options are each in their own group. There is also a navigation bar with an upload button. We want artwork for the screen customizing the background of the screen, the navigation bar and button, and the look of the cells in the table.

Screens should be submitted in unflattened PSD format.

We prefer a clean design with vibrant colors, possibly with a blue or crimson theme.

Please message me for details including the name of the service.

Thank you for helping with this project!

Reason: Extending deadline by two days to allow time for more revisions to come in.

Reason: Extending deadline to allow time for final designs.

Store

• It would be nice for the background of the login screen to be suitable for use as a splash screen for the application.

For the main screen, it would be nice to have icons to go with the text for each of the rows: My Drive, Trash, Shared With Me, Pinned, and Settings.

```html
<!DOCTYPE html>
<html lang="en">
<head>
<meta charset="utf-8">
<title>Cloud Storage – Main Screen</title>
<link href="https://fonts.googleapis.com/css2?family=PT+Sans:wght@400;700&display=swap" rel="stylesheet">
<style>
  :root{
    --page:#ffffff;
    --screen-bg:#ebebea;
    --header-bg:#f1f0ee;
    --cell-bg:#ffffff;
    --divider:#cdcdcd;
    --title-blue:#4d79a9;
    --sub-text:#3d3d3d;
    --icon-grey:#8b8b8b;
    --button-top:#6b93c4;
    --button-bottom:#3f6fa6;
    --status-bg:#dcdcdc;
    --status-text:#111111;
  }
  *{box-sizing:border-box;margin:0;padding:0}
  html,body{width:1200px;height:2263px;overflow:hidden;background:var(--page)}
  body{font-family:"PT Sans",sans-serif;position:relative}
  .screen{position:absolute;left:103px;top:410px;width:1001px;height:1492px;background:var(--screen-bg);overflow:hidden}
  .status-bar{position:absolute;left:0;top:0;width:100%;height:56px;background:var(--status-bg);border-bottom:2px solid #b9b9b9;color:var(--status-text);font-size:34px;font-weight:700}
  .status-bar .carrier{position:absolute;left:14px;top:8px;display:flex;align-items:center;gap:14px}
  .status-bar .time{position:absolute;left:0;right:0;top:8px;text-align:center}
  .status-bar .battery{position:absolute;right:22px;top:14px}
  .nav-header{position:absolute;left:0;top:56px;width:100%;height:258px;background:var(--header-bg);border-bottom:2px solid var(--divider)}
  .brand{position:absolute;left:36px;top:86px;display:flex;align-items:center;gap:26px}
  .brand-mark{width:100px;height:100px;border-radius:50%;background:#c7d3e0}
  .brand-name{font-size:42px;font-weight:700;color:var(--title-blue)}
  .upload-button{position:absolute;left:822px;top:59px;width:155px;height:88px;border-radius:6px;background:linear-gradient(var(--button-top),var(--button-bottom));border:2px solid #35608f;display:flex;align-items:center;justify-content:center}
  .cell-group{position:absolute;left:0;width:100%;background:var(--cell-bg);border-top:2px solid var(--divider);border-bottom:2px solid var(--divider)}
  .group-main{top:314px;height:592px}
  .group-pinned{top:980px;height:160px}
  .group-settings{top:1138px;height:166px}
  .cell{position:relative;height:196px;border-bottom:2px solid var(--divider)}
  .cell:last-child{border-bottom:none}
  .group-pinned .cell,.group-settings .cell{height:100%}
  .cell-title{position:absolute;left:93px;top:44px;font-size:60px;color:var(--title-blue);line-height:1}
  .cell-sub{position:absolute;left:93px;top:122px;font-size:31px;color:var(--sub-text);line-height:1}
  .cell-single .cell-title{top:50%;transform:translateY(-50%)}
  .cell-icon{position:absolute;left:870px;top:50%;transform:translateY(-50%);width:60px;height:60px}
</style>
</head>
<body>
<main class="screen">
  <div class="status-bar">
    <div class="carrier">
      <span>.....</span><span>Veo-UK</span>
      <svg width="40" height="32" viewBox="0 0 40 32"><path d="M4 12a23 23 0 0 1 32 0M10 18a14 14 0 0 1 20 0M16 24a6 6 0 0 1 8 0" fill="none" stroke="#2a7ad8" stroke-width="4" stroke-linecap="round"/></svg>
      <svg width="34" height="34" viewBox="0 0 34 34"><g stroke="#555" stroke-width="4" stroke-linecap="round"><path d="M17 3v7M17 24v7M3 17h7M24 17h7M7 7l5 5M22 22l5 5M7 27l5-5M22 12l5-5"/></g></svg>
    </div>
    <div class="time">08:17</div>
    <svg class="battery" width="66" height="30" viewBox="0 0 66 30"><rect x="2" y="2" width="56" height="26" rx="3" fill="none" stroke="#222" stroke-width="3"/><rect x="58" y="9" width="6" height="12" fill="#222"/><rect x="7" y="7" width="46" height="16" fill="#3fae2a"/></svg>
  </div>

  <header class="nav-header">
    <div class="brand">
      <span class="brand-mark"></span>
      <span class="brand-name">Cloud Storage</span>
    </div>
    <div class="upload-button" aria-label="Upload">
      <svg width="44" height="50" viewBox="0 0 44 50"><path d="M22 2 4 22h12v26h12V22h12z" fill="#fff"/></svg>
    </div>
  </header>

  <section class="cell-group group-main">
    <div class="cell">
      <div class="cell-title">My Drive</div>
      <div class="cell-sub">Is a data storage device</div>
      <svg class="cell-icon" viewBox="0 0 60 60"><path d="M6 16h18l5 6h25v26H6z" fill="var(--icon-grey)"/></svg>
    </div>
    <div class="cell">
      <div class="cell-title">Trash</div>
      <div class="cell-sub">Deleted, unnecessary files</div>
      <svg class="cell-icon" viewBox="0 0 60 60"><g fill="var(--icon-grey)"><rect x="12" y="10" width="36" height="6" rx="2"/><rect x="24" y="5" width="12" height="6" rx="2"/><path d="M15 19h30l-3 35H18z"/></g><g stroke="#fff" stroke-width="2.5"><path d="M24 24v25M30 24v25M36 24v25"/></g></svg>
    </div>
    <div class="cell">
      <div class="cell-title">Shared with Me</div>
      <div class="cell-sub">Files that are shared with me</div>
      <svg class="cell-icon" viewBox="0 0 60 60"><path d="M22 8h16v22h10L30 52 12 30h10z" fill="var(--icon-grey)"/></svg>
    </div>
  </section>

  <section class="cell-group group-pinned">
    <div class="cell cell-single">
      <div class="cell-title">Pinned</div>
      <svg class="cell-icon" viewBox="0 0 60 60"><path d="M6 32l8-8 10 10L48 8l8 8-32 34z" fill="var(--icon-grey)"/></svg>
    </div>
  </section>

  <section class="cell-group group-settings">
    <div class="cell cell-single">
      <div class="cell-title">Settings</div>
      <svg class="cell-icon" viewBox="0 0 60 60"><circle cx="30" cy="30" r="20" fill="none" stroke="var(--icon-grey)" stroke-width="10" stroke-dasharray="8 7.7"/><circle cx="30" cy="30" r="16" fill="none" stroke="var(--icon-grey)" stroke-width="9"/><circle cx="30" cy="30" r="6" fill="var(--cell-bg)"/></svg>
    </div>
  </section>
</main>
</body>
</html>
```